LUMO Electrical Services Letter Head

I need a professional clean looking design that will incorporate my company logo and information such as postal address, website, contact email "service@lumoelectrical.com.au" and phone number.

somewhere on the document i will also require my electrical contractor number "EC 047362" and my Australian Business number "57 193 640 208" these have to legally be on the document so they dont need to be a main feature, maybe in the footer in a smaller text.

Can you also have the 3 blue dashes from my logo as the watermark.

I would like the colour scheme to match my logo, business card and website www.lumoelectrical.com.au

I have the JPEG and PNG files for my logo which it will not allow me to upload as they are too wide, if you require these please let me know.

Target Market(s)

To be used for quotes and letters to commercial clients

Industry/Entity Type

Electric Company

Colors
0555a3
3176b5
85acd3
cfdfed
eaf1f7

Requirements
Must have
• company logo and information such as postal address, website, contact email "service@lumoelectrical.com.au" and phone number.
• somewhere on the document i will also require my electrical contractor number "EC 047362" and my Australian Business number "57 193 640 208" these have to legally be on the document so they dont need to be a main feature, maybe in the footer in a smaller text.
• I would like the colour scheme to match my logo, business card and website www.lumoelectrical.com.au
Nice to have
• Can you also have the 3 blue dashes from my logo as the watermark.

```html
<!DOCTYPE html>
<html lang="en">
<head>
<meta charset="utf-8">
<title>LUMO Electrical Services Letterhead</title>
<link rel="stylesheet" href="https://fonts.googleapis.com/css2?family=Arimo:wght@400;700&family=Tinos&display=swap">
<style>
  :root {
    --backdrop: #ddd0b9;
    --paper: #ffffff;
    --brand-deep: #0f6db3;
    --brand-mid: #3176b5;
    --brand-bright: #3a9ad9;
    --brand-soft: #cfdfed;
    --brand-mist: #eaf1f7;
    --ink: #1e1e1e;
    --body-ink: #4a4a4a;
  }
  * { box-sizing: border-box; margin: 0; padding: 0; }
  html, body {
    width: 1200px; height: 900px; overflow: hidden;
    background: var(--backdrop);
  }
  .letterhead {
    position: absolute; left: 300px; top: 26px;
    width: 600px; height: 848px;
    background: var(--paper);
    overflow: hidden;
  }
  .brand {
    position: absolute; left: 34px; top: 40px;
    font-family: "Tinos", serif; color: var(--ink);
  }
  .brand-name {
    font-family: "Arimo", sans-serif; font-weight: 700;
    font-size: 20px; letter-spacing: 0.5px; color: var(--ink);
    line-height: 1;
  }
  .brand-tagline {
    font-family: "Arimo", sans-serif; font-weight: 700;
    font-size: 8px; color: var(--ink); margin-top: 2px;
  }
  .legal-line { font-size: 12px; line-height: 12px; }
  .contact {
    position: absolute; right: 34px; top: 30px;
    font-family: "Tinos", serif; font-size: 11px; line-height: 11px;
    color: var(--ink); text-align: right;
  }
  .watermark {
    position: absolute; left: 240px; top: 295px;
    width: 130px; height: 80px;
  }
  .letter-body {
    position: absolute; left: 66px; top: 290px; width: 470px;
    font-family: "Arimo", sans-serif; font-size: 8.6px; line-height: 13px;
    color: var(--body-ink);
  }
  .letter-body p + p { margin-top: 13px; }
  .sign-off {
    position: absolute; right: 70px; top: 508px;
    font-family: "Arimo", sans-serif; font-size: 8.6px; color: var(--body-ink);
  }
  .signature-stamp {
    position: absolute; right: 62px; top: 528px;
    width: 62px; height: 62px;
  }
  .footer-wave {
    position: absolute; left: 0; bottom: 0; width: 600px; height: 220px;
  }
</style>
</head>
<body>
  <main class="letterhead">
    <header>
      <div class="brand">
        <div class="brand-name">LUMO</div>
        <div class="brand-tagline">Electrical Services</div>
        <div class="legal-line">Aus Business # 57 193 640 208</div>
        <div class="legal-line">EC 047362</div>
      </div>
      <address class="contact">
        Tel: 123-555-984<br>
        Mob: 123-456-78<br>
        Fax: 123-456-78<br>
        yourname@sample.com<br>
        www.yourcompany.com<br>
        Address Line 1<br>
        Address Line 2
      </address>
    </header>

    <svg class="watermark" viewBox="0 0 130 80" role="img" aria-label="Faint brand watermark area">
      <rect width="130" height="80" fill="var(--brand-mist)" opacity="0.7"/>
    </svg>

    <section class="letter-body">
      <p>Lorem ipsum dolor sit amet, consectetur adipiscing elit. Donec orci purus, luctus vitae dignissim eu, iaculis sed purus. Vivamus faucibus, ipsum nec aliquet viverra, leo mauris condimentum ligula, sit amet sagittis enim ligula quis arcu. Nam egestas tortor id nisi porttitor mattis. In tortor ante, ultricies in suscipit a, tempus non massa. Vivamus et auctor mi. Fusce vel massa nulla. Phasellus nec eros mauris, et scelerisque orci.</p>
      <p>Donec malesuada orci vitae nulla accumsan porta a id massa. Quisque accumsan iaculis magna sit amet fringilla. Maecenas consequat, magna eget tincidunt semper, odio nibh rutrum mi, id feugiat ante nisi eu risus. Vestibulum nunc orci, rhoncus a placerat in, ultricies in mi. Cras mattis varius eros, vel fringilla nisi suscipit eget. Quisque scelerisque sagittis nulla at porttitor.</p>
      <p>Sed id augue vitae urna euismod commodo aliquet a quam. Pellentesque arcu velit, cursus et malesuada ut, consequat et diam. Nullam erat sem, rhoncus id ullamcorper vitae, rhoncus et arcu. In ultricies ultricies nulla, ut rutrum nisi iaculis at. Donec eu magna a metus ornare faucibus. Fusce aliquet faucibus ultricies. Morbi semper, est id tincidunt gravida, sem arcu adipiscing lacus, ac bibendum nulla leo eu purus. Quisque nec diam sed risus consectetur accumsan quis quis nibh. Vestibulum id purus lorem.</p>
    </section>

    <div class="sign-off">Sincerely,</div>
    <svg class="signature-stamp" viewBox="0 0 62 62" role="img" aria-label="Handwritten signature over an official stamp">
      <circle cx="31" cy="31" r="28" fill="var(--brand-mist)" stroke="var(--brand-soft)" stroke-width="3"/>
    </svg>

    <svg class="footer-wave" viewBox="0 0 600 220" preserveAspectRatio="none" aria-hidden="true">
      <path d="M0,120 C180,110 400,100 600,20 L600,40 C460,110 300,140 0,150 Z" fill="var(--brand-bright)"/>
      <path d="M0,135 C200,128 420,110 600,42 L600,60 C470,140 280,170 0,220 Z" fill="var(--brand-deep)"/>
      <path d="M260,150 C420,120 520,90 600,48 L600,54 C520,100 420,130 260,150 Z" fill="var(--paper)"/>
      <path d="M180,160 C380,140 520,90 600,60 L600,220 L0,220 C60,200 120,175 180,160 Z" fill="var(--paper)"/>
      <path d="M200,158 C380,138 510,92 600,62" fill="none" stroke="var(--brand-bright)" stroke-width="3"/>
    </svg>
  </main>
</body>
</html>
```